New exciting tequila brand needs fun and attention drawing bottle label.

We need a design for on the glass bottle for a new tequila brand called "Comet Spin Tequila". It can be a label, or the decoration for the entire bottle.
The brand is called "Comet Spin" and is targeting a young party crowd.
I would like the visual to play with the image of a "tiger" & the idea of "up"side down.
In a bar the bottle needs to stand out, so it can be a very colourful design.

Good luck

Target Market(s)

young party crowd

Industry/Entity Type

Crowd

Colors
ec2027
fbed22
f37123
ffffff
f8ba93
fbf289

Requirements
Must have
• tiger
Nice to have
• play with the idea of upside down
Should not have
• have seen it before feeling

```html
<!DOCTYPE html>
<html lang="en">
<head>
<meta charset="utf-8">
<title>Comet Spin Tequila – Bottle Label</title>
<link rel="stylesheet" href="https://fonts.googleapis.com/css2?family=Tinos:wght@400;700&display=swap">
<style>
  :root {
    --page: #ffffff;
    --glass-light: #ffffff;
    --glass-mid: #ececec;
    --glass-edge: #c4c4c4;
    --cap-light: #f4f4f4;
    --cap-dark: #8a8a8a;
    --label-red: #e2001f;
    --label-pink: #f8ba93;
    --label-blush: #fbd6c2;
    --gold-light: #fbf289;
    --gold: #fbed22;
    --gold-mid: #e6b43a;
    --gold-deep: #b07d14;
    --ink: #111111;
  }
  html, body {
    margin: 0;
    padding: 0;
    width: 1200px;
    height: 3948px;
    overflow: hidden;
    background: var(--page);
  }
  .bottle-canvas {
    position: relative;
    width: 1200px;
    height: 3948px;
  }
  .bottle-art {
    display: block;
    width: 1200px;
    height: 3948px;
  }
  .brand-word {
    font-family: "Tinos", "Times New Roman", serif;
    font-weight: 700;
  }
  .brand-sub {
    font-family: "Tinos", "Times New Roman", serif;
    font-weight: 700;
    fill: var(--ink);
  }
</style>
</head>
<body>
<main class="bottle-canvas">
  <svg class="bottle-art" viewBox="0 0 1200 3948" xmlns="http://www.w3.org/2000/svg">
    <defs>
      <linearGradient id="glassBody" x1="0" x2="1" y1="0" y2="0">
        <stop offset="0" stop-color="var(--glass-mid)"/>
        <stop offset="0.12" stop-color="var(--glass-light)"/>
        <stop offset="0.85" stop-color="var(--glass-light)"/>
        <stop offset="1" stop-color="var(--glass-mid)"/>
      </linearGradient>
      <linearGradient id="capMetal" x1="0" x2="1" y1="0" y2="0">
        <stop offset="0" stop-color="var(--cap-dark)"/>
        <stop offset="0.35" stop-color="var(--cap-light)"/>
        <stop offset="0.65" stop-color="#d2d2d2"/>
        <stop offset="1" stop-color="var(--cap-dark)"/>
      </linearGradient>
      <linearGradient id="labelField" x1="0" x2="0" y1="0" y2="1">
        <stop offset="0" stop-color="var(--label-red)"/>
        <stop offset="0.33" stop-color="var(--label-red)"/>
        <stop offset="0.44" stop-color="var(--label-pink)"/>
        <stop offset="0.5" stop-color="var(--label-blush)"/>
        <stop offset="0.56" stop-color="var(--label-pink)"/>
        <stop offset="0.66" stop-color="var(--label-red)"/>
        <stop offset="1" stop-color="var(--label-red)"/>
      </linearGradient>
      <linearGradient id="goldFill" x1="0" x2="0" y1="0" y2="1">
        <stop offset="0" stop-color="var(--gold-light)"/>
        <stop offset="0.55" stop-color="var(--gold)"/>
        <stop offset="1" stop-color="var(--gold-deep)"/>
      </linearGradient>
      <linearGradient id="goldFrame" x1="0" x2="1" y1="0" y2="1">
        <stop offset="0" stop-color="var(--gold-deep)"/>
        <stop offset="0.5" stop-color="var(--gold-light)"/>
        <stop offset="1" stop-color="var(--gold-deep)"/>
      </linearGradient>
      <radialGradient id="tigerTone" cx="0.5" cy="0.4" r="0.65">
        <stop offset="0" stop-color="var(--gold-light)"/>
        <stop offset="0.55" stop-color="var(--gold-mid)"/>
        <stop offset="1" stop-color="var(--gold-deep)"/>
      </radialGradient>
      <clipPath id="labelClip">
        <rect x="237" y="1810" width="730" height="1430" rx="6"/>
      </clipPath>
    </defs>

    <!-- glass bottle -->
    <g class="bottle-glass">
      <path d="M433 360 L433 1040 C433 1180 150 1300 150 1560 L150 3760 C150 3810 180 3840 230 3840 L987 3840 C1037 3840 1067 3810 1067 3760 L1067 1560 C1067 1300 783 1180 783 1040 L783 360 Z"
            fill="url(#glassBody)" stroke="var(--glass-edge)" stroke-width="10"/>
      <path d="M190 1600 L190 3760" stroke="#dcdcdc" stroke-width="8" fill="none"/>
      <path d="M1030 1600 L1030 3760" stroke="#e0e0e0" stroke-width="8" fill="none"/>
      <path d="M360 1520 C470 1460 620 1460 720 1520" stroke="#d4d4d4" stroke-width="6" fill="none"/>
      <path d="M470 420 L470 1020" stroke="#e2e2e2" stroke-width="8" fill="none"/>
      <path d="M150 3690 C350 3730 870 3730 1067 3690" stroke="#dddddd" stroke-width="6" fill="none"/>
    </g>

    <!-- screw cap -->
    <g class="bottle-cap">
      <rect x="417" y="133" width="376" height="234" rx="36" fill="url(#capMetal)" stroke="#999999" stroke-width="6"/>
      <rect x="420" y="136" width="370" height="36" rx="18" fill="#e8e8e8"/>
      <line x1="421" y1="290" x2="789" y2="290" stroke="#777777" stroke-width="8"/>
      <line x1="421" y1="318" x2="789" y2="318" stroke="#777777" stroke-width="8"/>
      <line x1="421" y1="346" x2="789" y2="346" stroke="#777777" stroke-width="8"/>
    </g>

    <!-- label -->
    <g class="label">
      <rect class="label-frame" x="227" y="1800" width="750" height="1450" rx="12" fill="url(#goldFrame)"/>
      <rect class="label-field" x="237" y="1810" width="730" height="1430" rx="6" fill="url(#labelField)"/>

      <g clip-path="url(#labelClip)">
        <path class="tiger-top" role="img" aria-label="Illustration of a gold and black striped tiger crawling down from the top right corner"
              d="M700 1810 L967 1810 L967 2470 C930 2490 880 2470 868 2420 C860 2360 880 2300 860 2260 C820 2250 760 2230 720 2190 C680 2140 650 2080 660 2010 C665 1950 650 1880 700 1810 Z"
              fill="url(#tigerTone)"/>
        <path class="tiger-bottom" role="img" aria-label="Illustration of the same tiger upside down, climbing up from the bottom left corner"
              d="M237 2540 C280 2530 330 2560 340 2620 C350 2690 330 2760 350 2800 C400 2810 470 2840 510 2890 C560 2950 580 3030 570 3110 C565 3170 575 3210 560 3240 L237 3240 Z"
              fill="url(#tigerTone)"/>
      </g>

      <g class="wordmark">
        <text class="brand-word" x="283" y="2383" font-size="170" textLength="567" lengthAdjust="spacingAndGlyphs" fill="url(#goldFill)" stroke="#8a6410" stroke-width="2">COMET</text>
        <text class="brand-word" x="283" y="2503" font-size="130" textLength="250" lengthAdjust="spacingAndGlyphs" fill="url(#goldFill)" stroke="#8a6410" stroke-width="2">SPIN</text>
        <text class="brand-sub" x="548" y="2503" font-size="72">Tequila</text>
      </g>

      <g class="wordmark wordmark-flipped" transform="rotate(180 603 2523)">
        <text class="brand-word" x="283" y="2383" font-size="170" textLength="567" lengthAdjust="spacingAndGlyphs" fill="url(#goldFill)" stroke="#8a6410" stroke-width="2">COMET</text>
        <text class="brand-word" x="283" y="2503" font-size="130" textLength="250" lengthAdjust="spacingAndGlyphs" fill="url(#goldFill)" stroke="#8a6410" stroke-width="2">SPIN</text>
        <text class="brand-sub" x="548" y="2503" font-size="72">Tequila</text>
      </g>
    </g>
  </svg>
</main>
</body>
</html>
```